Sightless Fellowship Hall of San Diego needs an ad/flyer for convention program

Established in 1949, the Sightless Fellowship Hall of San Diego's mission is to enrich the lives of blind and visually impaired adults by preparing them for a normal, active life in a society that is principally sighted by encouraging independence.

Located in Harwick Gardens in San Diego, California, we are a nonprofit that gives blind and visually impaired people in our community an opportunity to socialize and interact. We help members build skills, confidence, and self-esteem through our various social, recreational, and educational activities. We were founded partially by Heron Guild members and receive ongoing funding from them.

We need an 8 1/2 by 11 inch color ad in jpg format. We would like it to be editable. This will be the foundation of our rebranding. The ad will be in a meeting program of the California Herons (californiaherons.example) with the goal of highlighting some of our programs in order to solicit donations from individual Heron Guilds, preferably ongoing ones.

We would like the ad to be generic enough that we can use the ad for other events and as a flyer in the future. We want the ad/flyer to be classic but eye popping with color. We want the design to reflect a professional and lively organization that loves to serve our members. We don’t entirely love our logo, but it’s what we have for now. Our next task will be a new logo design.

We would like to highlight some of our programs for our members include bingo, blind waterskiing and surfing, cooking and ceramic classes, foreign language classes, self defense classes, yoga, and craft classes. Many of the crafts our members make are sold during fundraisers, and they include blankets, scarves, beaded animals, and more. See a sampling of pictures. We provide transportation to and from our Center, free lunch while at the Center, and food to take home. Many of these activities continue during the pandemic via online platforms. We are doing monthly home deliveries of food to our members.

We need donations to keep our programs going, and we have building repairs & maintenance that we need donations in order to complete. See attached document regarding donations. Please reach out if you have questions. Thank you.

Web address: sfhsd.example
Street address: The Sightless Fellowship Hall of San Diego, 2716 Merrow St San Diego, CA 92107
Email address: donation@sfhsd.example
To make a donation: https://sfhsd.example/donate-2/

Donors

NonProfit

Sans Serif

Must have
• Highlight programs and information on how to make a donation.
Nice to have
• Information on how much each dollar donated will go - see attachment
Should not have
• Unprofessional or sloppy details

```html
<!DOCTYPE html>
<html lang="en">
<head>
<meta charset="utf-8">
<title>Sightless Fellowship Hall of San Diego – Convention Program Flyer</title>
<link rel="stylesheet" href="https://fonts.googleapis.com/css2?family=Montserrat:wght@400;500;600;700;800&display=swap">
<style>
  :root {
    --navy: #0d3470;
    --yellow: #e6dc12;
    --mustard: #d2c72a;
    --green: #7cb342;
    --orange: #f39a22;
    --sky: #1fa6df;
    --ink: #1d1d1d;
    --grey-text: #3a3a3a;
    --panel-border: #d5d5d5;
    --backdrop: #ececec;
    --paper: #ffffff;
  }
  * { box-sizing: border-box; margin: 0; padding: 0; }
  html, body { width: 1200px; height: 3123px; overflow: hidden; }
  body { background: var(--backdrop); font-family: "Montserrat", Arial, sans-serif; color: var(--ink); position: relative; }

  .flyer {
    position: absolute; left: 48px; top: 845px;
    width: 736px; height: 955px;
    background: var(--paper);
    transform: scale(1.5); transform-origin: top left;
    overflow: hidden;
  }
  .abs { position: absolute; }

  /* header */
  .brand-box { left: 0; top: 0; width: 208px; height: 112px; display: flex; align-items: center; justify-content: center; gap: 8px; }
  .brand-box .mark { width: 16px; height: 16px; background: var(--navy); }
  .brand-box .name { font-weight: 800; font-size: 40px; color: var(--navy); letter-spacing: 2px; }
  .header-band { left: 208px; top: 0; width: 528px; height: 112px; background: var(--navy); padding: 30px 0 0 14px; }
  .header-band .org { font-weight: 700; font-size: 17.5px; color: #fff; letter-spacing: 0.3px; white-space: nowrap; }
  .header-band .org span { color: var(--yellow); }
  .header-band .title { font-weight: 700; font-size: 37px; color: #fff; line-height: 1.05; letter-spacing: 0.5px; white-space: nowrap; }
  .side-navy { left: 697px; top: 112px; width: 39px; height: 48px; background: var(--navy); }
  .side-yellow { left: 705px; top: 160px; width: 31px; height: 270px; background: var(--mustard); }

  .hero-photo { left: 5px; top: 120px; width: 558px; height: 310px; background: linear-gradient(120deg, #6b4a34 0%, #b98d62 35%, #5a86b8 55%, #d9b896 80%, #7b6a5a 100%); }
  .thumb { left: 570px; width: 127px; }
  .thumb-1 { top: 120px; height: 102px; background: linear-gradient(160deg, #d8a9c6, #9e9cc9 60%, #c4b3d6); }
  .thumb-2 { top: 230px; height: 103px; background: linear-gradient(180deg, #dcdcdc, #2a3f9e 75%, #e6e6e6); }
  .thumb-3 { top: 338px; height: 92px; background: linear-gradient(180deg, #efefef, #3b3b3b 60%, #c8c8c8); }

  /* did you know */
  .info-band { left: 0; top: 430px; width: 736px; height: 56px; background: var(--navy); }
  .info-heading { left: 33px; top: 439px; font-weight: 800; font-size: 30px; color: var(--yellow); letter-spacing: 0.5px; }

  .fact-rail { left: 51px; top: 520px; width: 0; height: 215px; border-left: 1.5px dashed #9aa6bd; }
  .fact { left: 30px; width: 330px; display: flex; gap: 12px; }
  .fact .num { flex: none; width: 42px; height: 42px; border-radius: 50%; background: var(--yellow); display: flex; align-items: center; justify-content: center; }
  .fact .num span { width: 32px; height: 32px; border-radius: 50%; background: var(--navy); color: #fff; font-weight: 700; font-size: 15px; display: flex; align-items: center; justify-content: center; }
  .fact p { font-size: 8.6px; line-height: 1.32; color: var(--grey-text); padding-top: 1px; }
  .fact p b { color: var(--navy); font-weight: 700; }
  .fact p strong { color: var(--ink); font-weight: 700; }
  .fact-1 { top: 502px; } .fact-2 { top: 566px; } .fact-3 { top: 626px; }
  .fact-5 { top: 666px; } .fact-6 { top: 711px; }

  .every-dollar { left: 37px; top: 795px; font-weight: 600; font-size: 14.5px; line-height: 1.3; }

  /* pre-covid panel */
  .panel { left: 372px; top: 440px; width: 334px; height: 352px; border: 3px solid var(--panel-border); border-radius: 12px; background: #fff; overflow: hidden; }
  .panel-head { height: 44px; background: var(--yellow); display: flex; align-items: center; justify-content: center; font-weight: 800; font-size: 27px; color: var(--navy); letter-spacing: 0.5px; }
  .tier { display: flex; height: 76px; border-bottom: 1px solid #dcdcdc; }
  .tier:last-child { border-bottom: 0; height: 74px; }
  .tier .amount { width: 112px; flex: none; color: #fff; padding: 10px 0 0 12px; font-weight: 700; position: relative; }
  .amount .big { font-size: 21px; line-height: 1; }
  .amount .big sup { font-size: 9px; vertical-align: 9px; margin-right: 2px; }
  .amount .tag { font-size: 7px; line-height: 1; display: inline-block; margin-left: 4px; vertical-align: 4px; }
  .amount .or { font-size: 7px; display: block; margin: 1px 0 0 10px; line-height: 1; }
  .green { background: var(--green); } .orange { background: var(--orange); } .sky { background: var(--sky); }
  .tier ul { list-style: none; padding: 8px 6px 0 10px; display: flex; flex-direction: column; gap: 8px; justify-content: center; }
  .tier li { display: flex; gap: 6px; font-size: 7.6px; line-height: 1.25; font-weight: 500; color: var(--ink); }
  .tier li svg { flex: none; margin-top: 1px; }

  .lunch-note { left: 378px; top: 810px; font-weight: 600; font-size: 13.5px; line-height: 1.3; }

  /* donate bar */
  .donate-bar { left: 33px; top: 852px; width: 664px; height: 31px; border: 2px solid var(--navy); border-radius: 5px; overflow: hidden; display: flex; }
  .donate-bar .label { width: 292px; font-weight: 600; font-size: 20px; display: flex; align-items: center; justify-content: center; }
  .donate-bar .url { flex: 1; background: var(--yellow); font-weight: 700; font-size: 18px; color: var(--navy); display: flex; align-items: center; justify-content: center; }

  /* footer */
  .footer { left: 33px; top: 900px; width: 664px; height: 34px; display: flex; align-items: center; justify-content: space-between; font-weight: 600; font-size: 10.5px; }
  .footer .item { display: flex; align-items: center; gap: 8px; line-height: 1.3; }
  .footer .divider { width: 0; height: 32px; border-left: 1.5px dashed #777; }
</style>
</head>
<body>
<div class="flyer">
  <div class="abs brand-box"><span class="mark"></span><span class="name">SFH</span></div>
  <div class="abs header-band">
    <div class="org">SIGHTLESS FELLOWSHIP <span>HALL OF SAN DIEGO</span></div>
    <div class="title">CONVENTION PROGRAM</div>
  </div>
  <div class="abs side-navy"></div>
  <div class="abs side-yellow"></div>

  <div class="abs hero-photo" role="img" aria-label="Photo of a smiling boy holding hands with two caregivers in a library"></div>
  <div class="abs thumb thumb-1" role="img" aria-label="Photo of stacked handmade crocheted blankets"></div>
  <div class="abs thumb thumb-2" role="img" aria-label="Photo of a beaded angel ornament made in craft class"></div>
  <div class="abs thumb thumb-3" role="img" aria-label="Photo of a beaded penguin figure with a red hat"></div>

  <div class="abs info-band"></div>
  <div class="abs info-heading">DID YOU KNOW?</div>

  <div class="abs fact-rail"></div>
  <div class="abs fact fact-1"><div class="num"><span>01</span></div><p>During the pandemic we offer Bingo, Trivia and other virtual games every week, where blind and low vision participants can win SFH bucks. <b>You can sponsor one day of games for $35.</b></p></div>
  <div class="abs fact fact-2"><div class="num"><span>02</span></div><p>You can provide 75 gift bags for our ‘We are in This Together’ home delivery program. Many of our blind and low vision people are isolated and stuck at home. These gift packages are welcomed with enthusiasm and gratefulness. Your rewards are huge smiles and happy faces.</p></div>
  <div class="abs fact fact-3"><div class="num"><span>03</span></div><p>Our building is over 20 years old and requires ongoing maintenance and repairs</p></div>
  <div class="abs fact fact-5"><div class="num"><span>05</span></div><p><strong>Fencing (cage) required to protect outside air conditioning units from vandalism.</strong><br><b>Cost: $2,500</b></p></div>
  <div class="abs fact fact-6"><div class="num"><span>06</span></div><p>Wanted: Sponsors for weekly virtual bingo and trivia games: Blind and Low vision participants receive one SFH buck per win. SFH bucks are turned into gift cards and CTR transportation passes. <b>Sponsor one week for $40. Sponsor 1 month for $160</b></p></div>

  <div class="abs every-dollar">Every dollar donated goes to support<br>SFH participants and programs.</div>

  <div class="abs panel">
    <div class="panel-head">PRE-COVID:</div>
    <div class="tier">
      <div class="amount green"><span class="big"><sup>$</sup>10</span><span class="tag">PER<br>MONTH</span><span class="or">OR</span><span class="big"><sup>$</sup>120</span><span class="tag">WILL<br>BUY:</span></div>
      <ul>
        <li><svg width="8" height="8" viewBox="0 0 8 8"><circle cx="4" cy="4" r="4" fill="#0d3470"/><path d="M2 4.1l1.4 1.4L6 2.8" stroke="#fff" stroke-width="1.1" fill="none"/></svg>60 meals for our lunch program – we serve 130 meals each week</li>
        <li><svg width="8" height="8" viewBox="0 0 8 8"><circle cx="4" cy="4" r="4" fill="#0d3470"/><path d="M2 4.1l1.4 1.4L6 2.8" stroke="#fff" stroke-width="1.1" fill="none"/></svg>13 round trip CTR transportation tickets</li>
        <li><svg width="8" height="8" viewBox="0 0 8 8"><circle cx="4" cy="4" r="4" fill="#0d3470"/><path d="M2 4.1l1.4 1.4L6 2.8" stroke="#fff" stroke-width="1.1" fill="none"/></svg>Enough beads to make 35 Rosa Belle angels in our craft class</li>
      </ul>
    </div>
    <div class="tier">
      <div class="amount orange"><span class="big"><sup>$</sup>20</span><span class="tag">PER<br>MONTH</span><span class="or">OR</span><span class="big"><sup>$</sup>240</span><span class="tag">WILL<br>BUY:</span></div>
      <ul>
        <li><svg width="8" height="8" viewBox="0 0 8 8"><circle cx="4" cy="4" r="4" fill="#0d3470"/><path d="M2 4.1l1.4 1.4L6 2.8" stroke="#fff" stroke-width="1.1" fill="none"/></svg>26 round trip CTR transportation tickets</li>
        <li><svg width="8" height="8" viewBox="0 0 8 8"><circle cx="4" cy="4" r="4" fill="#0d3470"/><path d="M2 4.1l1.4 1.4L6 2.8" stroke="#fff" stroke-width="1.1" fill="none"/></svg>One month of large print and Braille translation newsletter printing</li>
      </ul>
    </div>
    <div class="tier">
      <div class="amount sky"><span class="big"><sup>$</sup>50</span><span class="tag">PER<br>MONTH</span><span class="or">OR</span><span class="big"><sup>$</sup>600</span><span class="tag">WILL<br>BUY:</span></div>
      <ul>
        <li><svg width="8" height="8" viewBox="0 0 8 8"><circle cx="4" cy="4" r="4" fill="#0d3470"/><path d="M2 4.1l1.4 1.4L6 2.8" stroke="#fff" stroke-width="1.1" fill="none"/></svg>300 lunches</li>
        <li><svg width="8" height="8" viewBox="0 0 8 8"><circle cx="4" cy="4" r="4" fill="#0d3470"/><path d="M2 4.1l1.4 1.4L6 2.8" stroke="#fff" stroke-width="1.1" fill="none"/></svg>Thanksgiving dinner with all the fixings for 80 to 100 guests</li>
      </ul>
    </div>
    <div class="tier">
      <div class="amount green"><span class="big"><sup>$</sup>100</span><span class="tag">PER<br>MONTH</span><span class="or">OR</span><span class="big"><sup>$</sup>1200</span><span class="tag">WILL<br>BUY:</span></div>
      <ul>
        <li><svg width="8" height="8" viewBox="0 0 8 8"><circle cx="4" cy="4" r="4" fill="#0d3470"/><path d="M2 4.1l1.4 1.4L6 2.8" stroke="#fff" stroke-width="1.1" fill="none"/></svg>Approximately 10 Bingo parties including food and prizes</li>
      </ul>
    </div>
  </div>

  <div class="abs lunch-note">$1,083 per month or $13,000 per year will<br>fund our entire lunch program for the year.</div>

  <div class="abs donate-bar">
    <div class="label">To make a donation:</div>
    <div class="url">https://sfhsd.example/donate-2/</div>
  </div>

  <div class="abs footer">
    <div class="item">
      <svg width="18" height="16" viewBox="0 0 18 16"><rect x="1" y="3" width="16" height="12" fill="none" stroke="#1d1d1d" stroke-width="1.6"/><path d="M1 3l8 7 8-7" fill="none" stroke="#1d1d1d" stroke-width="1.6"/></svg>
      donation@sfhsd.example
    </div>
    <div class="divider"></div>
    <div class="item">
      <svg width="16" height="20" viewBox="0 0 16 20"><path d="M8 1a6 6 0 0 0-6 6c0 4.5 6 11 6 11s6-6.5 6-11a6 6 0 0 0-6-6z" fill="none" stroke="#1d1d1d" stroke-width="1.6"/><circle cx="8" cy="7" r="2.2" fill="#1d1d1d"/></svg>
      <span>The Sightless Fellowship Hall of San Diego,<br>2716 Merrow St San Diego, CA 92107</span>
    </div>
    <div class="divider"></div>
    <div class="item">
      <svg width="18" height="18" viewBox="0 0 18 18"><circle cx="9" cy="9" r="8" fill="none" stroke="#1d1d1d" stroke-width="1.5"/><ellipse cx="9" cy="9" rx="3.5" ry="8" fill="none" stroke="#1d1d1d" stroke-width="1.2"/><path d="M1 9h16M2.5 5h13M2.5 13h13" stroke="#1d1d1d" stroke-width="1.1"/></svg>
      sfhsd.example
    </div>
  </div>
</div>
</body>
</html>
```